Cat-products company needs smart, yet endearing, business card

We need a business card design for a new, but up-and-running, business based in Honolulu, Hawaii. The business is Purrlane Nest Co. Our first product is the most environmentally-friendly cat grass kit ever seen on the planet. Future products, currently in the R&D phase, will include a variety of exciting cat scratchers. We also do consulting work to help apartment-dwellers make their home more cat-friendly and, in the future, plan on doing full, custom installs of structure to create high walkways for cats.

Target Market(s)

Middle-aged, apartment-dwelling, middle-class workers who own 1 or more cats and who dote on them.

Industry/Entity Type

Pet Care

Contact Information for Business Card

A striking, professional, yet warm and friendly design is what we're after.

Font styles to use
Serif
Sans Serif
Other font styles liked:
• Comfortaa

Colors

Designer to choose colors to be used in the design.

Requirements
Must have
• The company logo: (see attachment)
• The company name: Purrlane Nest Co
• The web address: www.purrlanenestco.example
• Email: support@purrlanenestco.example
• Phone: +1 (808) 555 0172
• Update (Fri Jun 30 3017 7:45pm Hawaii Time) I would like, is possible, uploaded picture of the cat grass kit on the back of the card with some text along the lines of: Purrlane Nest Co - Where The Freshest Kitty Sprouts Begin
Nice to have
• A cat picture, cartoon, real or silhouette that illustrates cats in action and/or relaxing; ie using the apartment space to live, play and relax in and being well-contented.
• Most of the website is done in the font: Comfortaa. It might be nice to continue using this for brand consistency.
Should not have
• Hard-to-read fonts.

```html
<!DOCTYPE html>
<html lang="en">
<head>
<meta charset="utf-8">
<title>Purrlane Nest Co – Business Card</title>
<link rel="stylesheet" href="https://fonts.googleapis.com/css2?family=Comfortaa:wght@500;700&family=Fredoka:wght@600&display=swap">
<style>
  :root {
    --amber: #f9b21b;
    --lemon: #f3e833;
    --cocoa: #583530;
    --white: #ffffff;
    --page: #ffffff;
  }
  * { box-sizing: border-box; margin: 0; padding: 0; }
  html, body { width: 1200px; height: 1000px; overflow: hidden; background: var(--page); }
  .canvas { position: relative; width: 1200px; height: 1000px; }

  .card {
    position: absolute;
    left: 297px;
    width: 606px;
    height: 346px;
    border-radius: 48px;
    overflow: hidden;
  }

  /* Front */
  .card--front {
    top: 87px;
    background:
      radial-gradient(circle at 479px 69px, var(--lemon) 0, rgba(243,232,51,0.55) 110px, rgba(249,178,27,0) 260px),
      var(--amber);
  }
  .front__photo {
    position: absolute;
    left: 0;
    bottom: 0;
    width: 420px;
    height: 170px;
    background: radial-gradient(ellipse at 45% 70%, rgba(252,200,70,0.75) 0, rgba(249,178,27,0) 70%);
  }
  .front__mark {
    position: absolute;
    left: 259px;
    top: 96px;
    width: 88px;
    height: 88px;
    background: var(--cocoa);
  }
  .front__name {
    position: absolute;
    left: 0;
    right: 0;
    top: 196px;
    text-align: center;
    font-family: "Fredoka", sans-serif;
    font-weight: 600;
    font-size: 40px;
    line-height: 48px;
    color: var(--white);
    letter-spacing: 0.5px;
  }

  /* Back */
  .card--back {
    top: 574px;
    background: var(--cocoa);
  }
  .back__band {
    position: absolute;
    left: 479px;
    top: 170px;
    right: 0;
    bottom: 0;
    background: var(--amber);
  }
  .back__name {
    position: absolute;
    left: 0;
    right: 0;
    top: 48px;
    text-align: center;
    font-family: "Fredoka", sans-serif;
    font-weight: 600;
    font-size: 40px;
    line-height: 48px;
    color: var(--amber);
    letter-spacing: 0.5px;
  }
  .contact {
    position: absolute;
    left: 120px;
    top: 178px;
    width: 350px;
    list-style: none;
    font-family: "Comfortaa", sans-serif;
    font-weight: 500;
    font-size: 15px;
    color: var(--white);
  }
  .contact__item {
    display: flex;
    align-items: center;
    justify-content: center;
    gap: 10px;
    height: 35px;
    white-space: nowrap;
  }
  .contact__item--web { color: var(--amber); }
  .contact__icon { width: 24px; height: 24px; flex: none; }
</style>
</head>
<body>
<main class="canvas">

  <section class="card card--front" aria-label="Business card front">
    <div class="front__photo" role="img" aria-label="Soft-toned photo of a relaxed kitten lying on the floor"></div>
    <div class="front__mark" aria-hidden="true"></div>
    <h1 class="front__name">Purrlane Nest Co</h1>
  </section>

  <section class="card card--back" aria-label="Business card back">
    <div class="back__band"></div>
    <h2 class="back__name">Purrlane Nest Co</h2>
    <ul class="contact">
      <li class="contact__item">
        <svg class="contact__icon" viewBox="0 0 24 24" aria-hidden="true">
          <path fill="#ffffff" d="M6.6 2.5c.6-.3 1.3-.1 1.6.5l2 3.6c.3.6.2 1.2-.3 1.6l-1.5 1.2c.9 2 2.5 3.7 4.5 4.6l1.2-1.5c.4-.5 1.1-.6 1.6-.3l3.6 2c.6.3.8 1 .5 1.6l-1 2c-.5 1-1.6 1.5-2.7 1.3C9.8 18 5.9 14.1 4.6 7.8c-.2-1.1.3-2.2 1.3-2.7z"/>
        </svg>
        <span>+1 (808) 555 0172</span>
      </li>
      <li class="contact__item">
        <svg class="contact__icon" viewBox="0 0 26 20" aria-hidden="true">
          <rect x="1" y="2" width="24" height="16" fill="#ffffff"/>
          <path d="M1 2l12 9 12-9M1 18l9-8M25 18l-9-8" fill="none" stroke="#583530" stroke-width="1.6"/>
        </svg>
        <span>support@purrlanenestco.example</span>
      </li>
      <li class="contact__item contact__item--web">
        <svg class="contact__icon" viewBox="0 0 24 24" aria-hidden="true">
          <circle cx="12" cy="12" r="10" fill="none" stroke="#f9b21b" stroke-width="2"/>
          <path d="M2 12h20M12 2c3 3 3 17 0 20M12 2c-3 3-3 17 0 20" fill="none" stroke="#f9b21b" stroke-width="1.6"/>
        </svg>
        <span>www.purrlanenestco.example</span>
      </li>
    </ul>
  </section>

</main>
</body>
</html>
```